Rack Card Design Project

www.nkcoldhaulers.com I am looking for a Rack Card for our Pick up/drop off and shipping purposes. So listed below are things I want on it.
Name, Address, Phone number, Credit Card info, Pickup or Drop off location, What the Item is, How many pieces or boxes. We are a hunting/ fishing company that specializes in Cold Storage and shipping of peoples fish and animals from Alaska. I added our company logo and also a Design of a Rack card so you can see what we are looking for.

```html
<!DOCTYPE html>
<html lang="en">
<head>
<meta charset="utf-8">
<title>NK Cold Haulers – Rack Card</title>
<link href="https://fonts.googleapis.com/css2?family=Roboto+Slab:wght@400;700;800&family=Mulish:wght@400&family=Ubuntu:wght@700&display=swap" rel="stylesheet">
<style>
  :root{
    --page:#e9e7e3;
    --card:#ffffff;
    --ink:#2b2b2b;
    --brand-red:#7a1c12;
    --label:#3a3a3a;
    --field:#ececec;
    --box-fill:#f7f1ea;
    --box-line:#8c8c8c;
    --forest-top:#efe7df;
    --forest-mid:#a58b78;
    --forest-low:#6d5545;
  }
  *{box-sizing:border-box;margin:0;padding:0}
  html,body{width:1200px;height:1200px;overflow:hidden;background:var(--page)}
  .rack-card{position:absolute;left:339px;top:28px;width:524px;height:1144px;background:var(--card);box-shadow:0 4px 18px rgba(0,0,0,.18);overflow:hidden}
  .forest-backdrop{position:absolute;left:0;top:520px;width:100%;height:624px;background:linear-gradient(180deg,#fff 0%,var(--forest-top) 18%,var(--forest-mid) 60%,var(--forest-low) 100%)}
  .hero-art{position:absolute;left:46px;top:58px;width:416px;height:196px;border-radius:4px;background:linear-gradient(100deg,#8a5a34 0%,#b98b5a 35%,#a9a9ad 60%,#c9606a 85%,#6e8a6a 100%)}
  .brand-name{position:absolute;left:0;width:100%;text-align:center;font-family:"Roboto Slab",serif;font-weight:800;color:var(--ink);line-height:1}
  .brand-name.main{top:262px;font-size:44px}
  .brand-name.sub{top:314px;font-size:26px}
  .tagline{position:absolute;left:40px;right:40px;top:384px;text-align:center;font-family:"Roboto Slab",serif;font-size:12px;line-height:15px;color:var(--brand-red)}
  .form-panel{position:absolute;left:38px;top:422px;width:440px;height:696px;background:var(--card);border-radius:14px 14px 0 0;box-shadow:0 -2px 10px rgba(0,0,0,.12)}
  .form-title{position:absolute;left:0;width:100%;top:28px;text-align:center;font-family:"Roboto Slab",serif;font-weight:700;font-size:17px;color:var(--brand-red)}
  .field-row{position:absolute;left:31px;right:32px;height:20px;display:flex;align-items:center;gap:8px;font-family:"Mulish",sans-serif;font-size:15px;color:var(--label);white-space:nowrap}
  .field-row .bar{flex:1;height:20px;background:var(--field)}
  .opt{position:absolute;display:flex;align-items:flex-start;gap:6px;font-family:"Mulish",sans-serif;font-size:15px;line-height:20px;color:var(--label);white-space:nowrap}
  .opt .tick-box{width:15px;height:15px;border:1.5px solid #333;margin-top:2px;flex:none;background:#fff}
  .option-group{position:absolute;border:2px solid var(--box-line);border-radius:6px;background:var(--box-fill)}
  .group-title{position:absolute;top:-13px;left:50%;transform:translateX(-50%);background:var(--card);padding:0 8px;font-family:"Roboto Slab",serif;font-weight:700;font-size:18px;color:var(--brand-red);white-space:nowrap;line-height:24px}
  .fill-line{position:absolute;height:19px;background:#fff}
  .site-url{position:absolute;left:0;width:100%;top:650px;text-align:center;font-family:"Ubuntu",sans-serif;font-weight:700;font-size:24px;line-height:30px;color:var(--brand-red)}
</style>
</head>
<body>
<main class="rack-card">
  <div class="forest-backdrop" role="img" aria-label="Faded forest of bare trees in warm brown tones"></div>
  <div class="hero-art" role="img" aria-label="Illustration of a moose, mountain sheep on a snowy peak and a leaping salmon"></div>
  <div class="brand-name main">NK COLD HAULERS</div>
  <div class="brand-name sub">LLC</div>
  <p class="tagline">We are a hunting/ fishing company that specializes in Cold Storage<br>and shipping of people’s fish and animals from Alaska.</p>

  <section class="form-panel">
    <h2 class="form-title">SHIPPING / PROCESSING INFORMATION</h2>
    <div class="field-row" style="top:62px">Name:<span class="bar"></span></div>
    <div class="field-row" style="top:89px">Address:<span class="bar"></span></div>
    <div class="field-row" style="top:116px">Cell Phone:<span class="bar"></span></div>
    <div class="field-row" style="top:143px">Home Phone:<span class="bar"></span></div>
    <div class="field-row" style="top:170px">Item(s):<span class="bar"></span></div>
    <div class="field-row" style="top:197px">No. of Pieces / Boxes:<span class="bar"></span></div>
    <div class="field-row" style="top:224px">Credit Card No.:<span class="bar"></span></div>
    <div class="opt" style="left:89px;top:254px"><span class="tick-box"></span>Nordpay</div>
    <div class="opt" style="left:223px;top:254px"><span class="tick-box"></span>Credex</div>

    <div class="option-group" style="left:24px;top:292px;width:392px;height:164px">
      <h3 class="group-title">Select Drop Off Service</h3>
      <div class="opt" style="left:18px;top:20px"><span class="tick-box"></span>Taxidermist</div>
      <div class="fill-line" style="left:134px;top:21px;width:238px"></div>
      <div class="opt" style="left:18px;top:48px"><span class="tick-box"></span>Meat Processor</div>
      <div class="fill-line" style="left:154px;top:49px;width:218px"></div>
      <div class="opt" style="left:18px;top:76px"><span class="tick-box"></span>Airport</div>
      <div class="fill-line" style="left:98px;top:77px;width:172px"></div>
      <div class="opt" style="left:277px;top:76px">Time</div>
      <div class="fill-line" style="left:314px;top:77px;width:58px"></div>
      <div class="opt" style="left:18px;top:104px"><span class="tick-box"></span>Hotel</div>
      <div class="fill-line" style="left:84px;top:105px;width:288px"></div>
      <div class="opt" style="left:18px;top:131px"><span class="tick-box"></span>Mail</div>
      <div class="opt" style="left:171px;top:131px"><span class="tick-box"></span>Cold Storage</div>
    </div>

    <div class="option-group" style="left:37px;top:482px;width:364px;height:150px">
      <h3 class="group-title">Shipping Options</h3>
      <div class="opt" style="left:20px;top:23px"><span class="tick-box"></span>Truck Ground<br>Shipping (Large<br>&amp; Crafted Items)</div>
      <div class="opt" style="left:20px;top:88px"><span class="tick-box"></span>Postal Mail</div>
      <div class="opt" style="left:20px;top:113px"><span class="tick-box"></span>Parcel Couriers</div>
      <div class="opt" style="left:186px;top:23px"><span class="tick-box"></span>International<br>Shipping</div>
      <div class="opt" style="left:186px;top:68px"><span class="tick-box"></span>Regional Air Cargo</div>
      <div class="opt" style="left:186px;top:95px"><span class="tick-box"></span>Overnight Shipping</div>
    </div>

    <p class="site-url">www.nkcoldhaulers.com</p>
  </section>
</main>
</body>
</html>
```